Website Design for a holiday home letting busines

We require a redesign of our present website www.fernbrookstays.com. We want the website to stand out and look professional and clean to make holiday hunters want to book a caravan or lodge holiday with us. Our logo is red however we DO NOT want the website to be red. We want a natural colour scheme.

The final design should communicate that we are a professional company to book with.

On the home page we require;
Overview of company
Photo
Search box for holiday (check in)
Late Deals
Reviews
News

We would like the following pages designed; home page, available dates page, caravans page, content page.

The website should be responsive for smart phones. One website I do like is http://www.brimoveld.be/nl/

Target Market(s)

Families

Industry/Entity Type

Travel

Number of Pages Required

5+ page

Font styles to use
Serif

Requirements
Must have
• The project must be responsive for mobile phones and tablets.
• Ability to search for holiday home holidays
• We want a natural colour scheme.
Nice to have
• A style we like is http://www.brimoveld.be/nl/
Should not have
• Do not use red as a colour for the website. Our logo is red so this is the only time we want this used.

```html
<!DOCTYPE html>
<html lang="en">
<head>
<meta charset="utf-8">
<title>Fernbrook Stays – Holiday Lodge &amp; Caravan Rentals</title>
<link href="https://fonts.googleapis.com/css2?family=Oswald:wght@400;600&family=Open+Sans:wght@400;600;700&display=swap" rel="stylesheet">
<style>
:root{
  --green:#5aa636;
  --green-dark:#3f8424;
  --blue:#3b8fcb;
  --orange:#d8733a;
  --orange-dark:#c4612b;
  --teal:#35b0ad;
  --purple:#8b5c9f;
  --gold:#ddb01e;
  --ink:#333;
  --muted:#777;
  --panel:#ffffff;
  --line:#e4e4e4;
  --card:#f4f4f4;
  --footer-dark:#2f3336;
  --logo:#333;
}
*{box-sizing:border-box;margin:0;padding:0}
html,body{width:1200px;height:3000px;overflow:hidden}
body{position:relative;font-family:"Open Sans",Arial,sans-serif;color:var(--ink);background:#fff}
.abs{position:absolute}

/* scenic backgrounds */
.scene-top{left:0;top:0;width:1200px;height:560px;background:
  radial-gradient(ellipse 420px 180px at 980px 440px,rgba(214,150,120,.55),transparent 70%),
  radial-gradient(ellipse 500px 160px at 820px 120px,rgba(120,90,60,.55),transparent 70%),
  linear-gradient(180deg,#7fa98a 0%,#56784a 35%,#3f5c3b 55%,#8ab0ad 72%,#5f8f93 100%)}
.scene-page{left:0;top:620px;width:1200px;height:2180px;background:
  radial-gradient(ellipse 260px 500px at 1120px 900px,rgba(110,80,60,.45),transparent 70%),
  radial-gradient(ellipse 220px 400px at 70px 820px,rgba(70,110,60,.6),transparent 70%),
  linear-gradient(180deg,#6fb9ea 0%,#a6d5f3 20%,#92bf8a 32%,#5f8a58 42%,#86bccb 56%,#4f9cb4 100%)}

/* top promo */
.promo-logo{left:0;width:1200px;top:168px;text-align:center;color:#fff;font-weight:700;font-size:22px;display:flex;justify-content:center;align-items:center;gap:10px}
.promo-logo .dot{width:30px;height:30px;border-radius:50%;background:#fff}
.promo-title{left:0;width:1200px;top:214px;text-align:center;color:#fff;font-family:"Oswald",sans-serif;font-weight:600;font-size:32px;line-height:42px;letter-spacing:.5px}
.promo-btn{left:490px;top:312px;width:220px;height:46px;background:var(--green);color:#fff;font-family:"Oswald",sans-serif;font-size:21px;line-height:46px;text-align:center;letter-spacing:1px}

/* nav */
.nav{left:0;top:560px;width:1200px;height:60px;background:#fff;display:flex;align-items:center;padding:0 180px}
.brand{display:flex;align-items:center;gap:8px;font-weight:700;color:var(--logo);font-size:18px}
.brand .dot{width:28px;height:28px;border-radius:50%;background:#c9c9c9}
.phone{margin-left:20px;font-size:13px;color:var(--muted);display:flex;gap:6px;align-items:center}
.menu{display:flex;gap:30px;margin-left:auto;font-size:13px;color:#555}
.menu .on{color:var(--ink);font-weight:700}
.connect{margin-left:30px;background:var(--teal);color:#fff;font-size:13px;padding:0 10px;height:36px;display:flex;align-items:center;gap:8px}
.connect .sq{width:22px;height:22px;background:#fff;opacity:.9}

/* hero */
.hero-text{left:180px;top:680px;width:400px;color:#fff}
.hero-text h1{font-family:"Oswald",sans-serif;font-weight:400;font-size:36px}
.hero-text p{font-size:16px;line-height:24px;margin-top:10px}
.hero-text .small{font-size:12px;line-height:18px;opacity:.92}
.more{display:inline-block;margin-top:16px;background:var(--orange);color:#fff;font-size:13px;padding:9px 20px}
.hero-photo{left:620px;top:650px;width:400px;height:300px;background:
  radial-gradient(circle at 35% 40%,#f3d08a 0 18%,transparent 40%),
  radial-gradient(circle at 70% 55%,#e58b7a 0 14%,transparent 38%),
  linear-gradient(135deg,#f0c25b,#3aa7c9 55%,#2b6f9e);clip-path:polygon(12% 4%,100% 0,90% 100%,0 88%)}
.dots{left:560px;top:962px;display:flex;gap:8px}
.dots i{width:10px;height:10px;border-radius:50%;background:#fff;opacity:.6;display:block}
.dots i.on{opacity:1}

/* panel */
.panel{left:180px;top:1000px;width:840px;height:1780px;background:var(--panel)}

/* search */
.search{left:180px;top:1000px;width:840px;height:56px;background:var(--green);display:flex;align-items:center;padding:0 20px;gap:18px}
.search h2{font-family:"Oswald",sans-serif;font-weight:400;color:#fff;font-size:24px}
.search .field{flex:1;height:32px;background:#fff}
.search .go{width:44px;height:32px;background:var(--orange);color:#fff;font-size:13px;font-weight:700;text-align:center;line-height:32px}

.heading{font-family:"Oswald",sans-serif;font-weight:600;text-align:center;letter-spacing:1px}
.overview{left:180px;top:1066px;width:840px}
.overview h2{color:var(--blue);font-size:32px}
.overview h2 span{color:var(--green)}
.overview p{font-size:12px;line-height:19px;color:var(--muted);text-align:center;margin:12px 70px 0}

.gallery{left:160px;top:1260px;width:880px;height:350px;background:linear-gradient(180deg,var(--orange),var(--orange-dark))}
.gallery h2{color:#fff;font-size:32px;margin-top:16px}
.gallery h2 small{font-size:32px;font-weight:400}
.g-grid{position:absolute;left:80px;top:82px;width:720px;display:grid;grid-template-columns:repeat(4,1fr);gap:16px}
.g-grid div{height:116px;border:4px solid #fff}
.arrow{position:absolute;top:150px;width:28px;height:28px;border-radius:50%;background:rgba(255,255,255,.85);display:flex;align-items:center;justify-content:center}

.deals{left:180px;top:1630px;width:840px}
.deals h2{color:var(--blue);font-size:34px}
.deals h2 span{color:var(--green)}
.deal-strip{margin:10px 30px 0;background:var(--green);color:#fff;font-size:11px;text-align:center;padding:8px;line-height:16px;font-weight:600}
.cards{display:flex;gap:26px;margin:22px 40px 0}
.card{flex:1;background:var(--card);border:1px solid var(--line)}
.card .ph{height:190px;margin:10px}
.card h3{font-size:15px;margin:0 12px}
.card .date{font-size:13px;color:var(--muted);margin:4px 12px 0}
.card .date b{color:var(--green)}
.spec{margin:12px 12px;font-size:12px;display:grid;grid-template-columns:1fr 1fr;gap:6px}
.spec div{background:#fff;padding:5px 6px;display:flex;align-items:center;gap:6px}
.spec div i{width:14px;height:12px;background:var(--teal);display:block}
.book{margin:10px 12px 12px;background:var(--green);color:#fff;font-size:13px;padding:9px;text-align:center}

.lower{left:180px;top:2160px;width:840px;display:flex;gap:34px;padding:0 20px}
.col h2{font-family:"Oswald",sans-serif;font-weight:600;font-size:32px;color:#555;border-bottom:2px solid var(--line);padding-bottom:6px;margin-bottom:18px}
.reviews{width:430px}
.review{margin-bottom:22px}
.review .who{font-size:11px;font-weight:700;letter-spacing:.5px;margin-bottom:5px}
.review .box{color:#fff;padding:14px 50px 14px 14px;min-height:86px;clip-path:polygon(0 0,91% 0,100% 50%,91% 100%,0 100%)}
.review .box b{font-size:15px;display:block;margin-bottom:4px}
.review .box span{font-size:12px;line-height:17px;display:block}
.news{flex:1}
.item{display:flex;gap:14px;margin-bottom:28px;align-items:flex-start}
.item .th{width:100px;height:100px;flex:none}
.item b{font-size:15px;display:block;margin-top:8px}
.item span{font-size:11px;color:var(--muted)}
.item p{font-size:12px;line-height:17px;color:var(--muted);margin-top:6px}

/* footer */
.chat{left:890px;top:2736px;width:120px;height:40px;background:var(--green);color:#fff;font-size:13px;line-height:40px;text-align:center}
.footer{left:0;top:2780px;width:1200px;height:180px;background:#fff;border-top:6px solid var(--teal)}
.f-brand{left:180px;top:2840px}
.f-cols{left:420px;top:2822px;display:flex;gap:40px;font-size:11px;line-height:16px;color:var(--muted)}
.f-social{left:810px;top:2840px;display:flex;gap:8px}
.f-social i{width:24px;height:24px;border-radius:50%;background:var(--teal);display:block}
.f-badge{left:900px;top:2812px;width:110px;height:110px;border-radius:50%;background:var(--green-dark)}
.bottom{left:0;top:2960px;width:1200px;height:40px;background:var(--footer-dark);color:#aaa;font-size:11px;display:flex;align-items:center;padding:0 180px;gap:20px}
.bottom .pay{display:flex;gap:6px;margin-left:260px}
.bottom .pay i{width:30px;height:18px;background:#888;display:block}
.bottom .credit{margin-left:auto}
</style>
</head>
<body>

<div class="abs scene-top" role="img" aria-label="Couple relaxing on a lodge deck beside a tree-lined lake"></div>

<div class="abs promo-logo"><span class="dot"></span>Fernbrook Stays</div>
<div class="abs promo-title">WOULD YOU LIKE TO BOOK A 2016 CARAVAN OR LODGE<br>HOLIDAY AT MARROW BAY HOLIDAY PARK</div>
<div class="abs promo-btn">LODGE HOLIDAY</div>

<header class="abs nav">
  <div class="brand"><span class="dot"></span>Fernbrook Stays</div>
  <div class="phone">
    <svg width="12" height="12" viewBox="0 0 24 24"><path fill="#777" d="M6.6 10.8a15 15 0 006.6 6.6l2.2-2.2a1 1 0 011-.25 11 11 0 003.5.56 1 1 0 011 1V20a1 1 0 01-1 1A17 17 0 013 4a1 1 0 011-1h3.5a1 1 0 011 1 11 11 0 00.56 3.5 1 1 0 01-.25 1z"/></svg>
    01632 960 418
  </div>
  <nav class="menu"><span class="on">Home</span><span>Available</span><span>Caravans</span><span>Content</span></nav>
  <div class="connect">Connect with us on <span class="sq"></span></div>
</header>

<div class="abs scene-page" role="img" aria-label="Blue sky over a lakeside holiday park with lodges and trees reflected in the water"></div>

<div class="abs hero-text">
  <h1>Private Holiday Rentals</h1>
  <p>Quality Lodge &amp; Caravan hire at Marrow Bay Holiday Park. Book online today!</p>
  <p class="small">Relax in a spacious lodge or caravan by the lake, with everything you need for a family break close at hand. Choose your dates, compare homes and book in just a few simple steps with our friendly team.</p>
  <span class="more">More Details</span>
</div>
<div class="abs hero-photo" role="img" aria-label="Happy family enjoying a holiday together"></div>
<div class="abs dots"><i></i><i class="on"></i><i></i><i></i><i></i></div>

<div class="abs panel"></div>

<div class="abs search">
  <h2>Search for Holiday</h2>
  <div class="field"></div>
  <div class="go">GO</div>
</div>

<section class="abs overview">
  <h2 class="heading">OVERVIEW <span>OF COMPANY</span></h2>
  <p>We are a family run business offering privately owned lodges and caravans at a beautiful lakeside park. Every home is cleaned, checked and ready for your arrival so you can simply relax and enjoy the break with the people you love.</p>
  <p>Our homes range from cosy two bedroom caravans to spacious luxury lodges with hot tubs and decking. Browse the photos, pick your dates and book securely online, or call our team who will be happy to help.</p>
</section>

<section class="abs gallery">
  <h2 class="heading">PHOTO <small>Fernbrook Stays</small></h2>
  <span class="arrow" style="left:26px"><svg width="10" height="10" viewBox="0 0 10 10"><path d="M7 1L3 5l4 4" stroke="#c4612b" stroke-width="2" fill="none"/></svg></span>
  <span class="arrow" style="right:26px"><svg width="10" height="10" viewBox="0 0 10 10"><path d="M3 1l4 4-4 4" stroke="#c4612b" stroke-width="2" fill="none"/></svg></span>
  <div class="g-grid">
    <div role="img" aria-label="Lodge exterior" style="background:linear-gradient(160deg,#a8926c,#6f5e44)"></div>
    <div role="img" aria-label="Lodge lounge" style="background:linear-gradient(160deg,#d2b88e,#94785a)"></div>
    <div role="img" aria-label="Park pool" style="background:linear-gradient(160deg,#8fd0e6,#2f8db3)"></div>
    <div role="img" aria-label="Family on the beach" style="background:linear-gradient(160deg,#9fd0ee,#e0c98f)"></div>
    <div role="img" aria-label="Children playing" style="background:linear-gradient(160deg,#e7b7a6,#b1786a)"></div>
    <div role="img" aria-label="Kitchen interior" style="background:linear-gradient(160deg,#c9ab82,#8d7052)"></div>
    <div role="img" aria-label="Bedroom interior" style="background:linear-gradient(160deg,#b8946c,#7b5b3f)"></div>
    <div role="img" aria-label="Lodge at dusk" style="background:linear-gradient(160deg,#8d86a8,#4f4a5e)"></div>
  </div>
</section>

<section class="abs deals">
  <h2 class="heading">LATE <span>DEALS</span></h2>
  <div class="deal-strip">LATE DEALS ON SELECTED HOMES – BOOK BEFORE THEY ARE GONE<br>LIMITED DATES LEFT THIS SEASON, CALL OR BOOK ONLINE</div>
  <div class="cards">
    <div class="card">
      <div class="ph" role="img" aria-label="Lodge interior" style="background:linear-gradient(150deg,#d9c7ae,#9b7f60)"></div>
      <h3>The Alderley</h3>
      <p class="date">Friday 17 September 2016 <b>(7 nights)</b></p>
      <div class="spec"><div><i></i>Caravan</div><div><i></i>Sleeps 4</div><div><i></i>2 Bedrooms</div><div><i></i>Decking</div></div>
      <div class="book">Book now for £199.00</div>
    </div>
    <div class="card">
      <div class="ph" role="img" aria-label="Lodge bedroom" style="background:linear-gradient(150deg,#e2d3bf,#a88a6a)"></div>
      <h3>The Alderley</h3>
      <p class="date">Friday 17 September 2016 <b>(7 nights)</b></p>
      <div class="spec"><div><i></i>Caravan</div><div><i></i>Sleeps 4</div><div><i></i>2 Bedrooms</div><div><i></i>Decking</div></div>
      <div class="book">Book now for £199.00</div>
    </div>
    <div class="card">
      <div class="ph" role="img" aria-label="Lodge kitchen" style="background:linear-gradient(150deg,#d6c3a8,#8e7358)"></div>
      <h3>The Alderley</h3>
      <p class="date">Friday 17 September 2016 <b>(7 nights)</b></p>
      <div class="spec"><div><i></i>Caravan</div><div><i></i>Sleeps 4</div><div><i></i>2 Bedrooms</div><div><i></i>Decking</div></div>
      <div class="book">Book now for £199.00</div>
    </div>
  </div>
</section>

<div class="abs lower">
  <section class="col reviews">
    <h2>REVIEWS</h2>
    <div class="review"><div class="who" style="color:var(--teal)">GLADYS WREN</div><div class="box" style="background:var(--teal)"><b>Stayed in the Alderley</b><span>Lovely clean lodge with everything we needed for the week, we will certainly book again next summer.</span></div></div>
    <div class="review"><div class="who" style="color:var(--purple)">TRACEY HOLM</div><div class="box" style="background:var(--purple)"><b>Stayed in the Alderley</b><span>The kids loved the park and the caravan was spotless on arrival, a brilliant family break.</span></div></div>
    <div class="review"><div class="who" style="color:var(--gold)">PAULA GREER</div><div class="box" style="background:var(--gold)"><b>Stayed in the Alderley</b><span>Friendly team, easy booking and a fantastic view of the lake from the decking.</span></div></div>
    <div class="review"><div class="who" style="color:var(--teal)">ALISON MARSH</div><div class="box" style="background:var(--teal)"><b>Stayed in the Alderley</b><span>Great value for a family break, comfortable beds and highly recommended to friends.</span></div></div>
  </section>
  <section class="col news">
    <h2>NEWS</h2>
    <div class="item"><div class="th" role="img" aria-label="Fireworks over the park" style="background:linear-gradient(150deg,#a35a8f,#4a2546)"></div><div><b>Fireworks Weekend</b><span>Posted on 18 August 2016</span><p>Join us by the lake for a night of music and colour.</p></div></div>
    <div class="item"><div class="th" role="img" aria-label="Live show on stage" style="background:linear-gradient(150deg,#e08a6c,#9e3f2e)"></div><div><b>Go Go Show Live at Marrow Bay</b><span>Posted on 10 August 2016</span><p>A fun live show for the whole family this month.</p></div></div>
    <div class="item"><div class="th" role="img" aria-label="Easter entertainer" style="background:linear-gradient(150deg,#e3c29c,#a67c55)"></div><div><b>Easter Family Games</b><span>Posted on 2 August 2016</span><p>Egg hunts, games and prizes around the park.</p></div></div>
    <div class="item"><div class="th" role="img" aria-label="Fireworks display" style="background:linear-gradient(150deg,#8a5ea6,#37224a)"></div><div><b>Fireworks Weekend</b><span>Posted on 24 July 2016</span><p>Book early to catch the best display of the year.</p></div></div>
  </section>
</div>

<div class="abs chat">Chat Now</div>
<footer class="abs footer"></footer>
<div class="abs f-brand brand"><span class="dot"></span>Fernbrook Stays</div>
<div class="abs f-cols">
  <div>About Us<br>Home<br>Available Dates<br>Caravans<br>Lodges</div>
  <div>Marrow Bay<br>Park Facilities<br>Things To Do<br>Late Deals<br>Contact</div>
  <div>Fernbrook Stays<br>Terms &amp; Conditions<br>Privacy Policy<br>Sitemap</div>
</div>
<div class="abs f-social"><i></i><i></i></div>
<div class="abs f-badge"></div>
<div class="abs bottom">
  <span>© 2016 Fernbrook Stays</span>
  <span class="pay"><i></i><i></i><i></i></span>
  <span class="credit">www.fernbrookstays.com</span>
</div>

</body>
</html>
```